Power Point Template

I would like to have a power point template for our company.
See our website: www.brevikhamna.se for logo/colors and inspiration.

The template will be used for bank meetings etc, so it should be formal and professional.

Should show examples of various layouts.
Updates

I want the following headings/sections/example slides: - Slide with table of contents - Slide with bullets (just to show how a bullet list looks like) - Slide with project timeline - Slide with business case calculations (table e.g.) - slide with pictures with room for descriptive text (to show inspirational pictures, one slide per section: exterior, interior upper floor, exterior lower floor)? - Slide where our buildings are described (bullet list) - Slide with presentation of our business partners - First page with a faded background picture of our building (the one where our logo is shown)

Industry/Entity Type

It Company

```html
<!DOCTYPE html>
<html lang="en">
<head>
<meta charset="utf-8">
<title>Our Team</title>
<link rel="stylesheet" href="https://fonts.googleapis.com/css2?family=Roboto+Condensed:wght@400;700&display=swap">
<style>
  :root {
    --page-bg: #f7f7f7;
    --navy: #1c2e4a;
    --accent: #f5a00c;
    --ring: #c4c4c4;
    --white: #ffffff;
    --footer-band: #7f8a96;
    --photo-light: #c9c2bf;
    --photo-dark: #8a6a58;
  }
  * { margin: 0; padding: 0; box-sizing: border-box; }
  html, body {
    width: 1200px;
    height: 900px;
    overflow: hidden;
    background: var(--page-bg);
  }
  .slide {
    position: relative;
    width: 1200px;
    height: 900px;
    background: var(--page-bg);
    font-family: "Roboto Condensed", "Arial Narrow", sans-serif;
    color: var(--navy);
  }
  .brand-name {
    position: absolute;
    top: 34px;
    right: 22px;
    font-size: 26px;
    font-weight: 700;
    color: var(--navy);
    letter-spacing: 0.5px;
  }
  .slide-title {
    position: absolute;
    top: 74px;
    left: 0;
    width: 1200px;
    text-align: center;
    font-size: 40px;
    font-weight: 400;
    color: #111111;
    letter-spacing: 0.5px;
  }
  .slide-title strong { font-weight: 700; }
  .title-rule {
    position: absolute;
    top: 126px;
    left: 396px;
    width: 408px;
    height: 4px;
    background: var(--navy);
  }
  .team-member {
    position: absolute;
    top: 278px;
    width: 340px;
    text-align: center;
  }
  .team-member.first { left: 38px; }
  .team-member.second { left: 429px; }
  .team-member.third { left: 832px; }
  .portrait-frame {
    width: 206px;
    height: 206px;
    margin: 0 auto;
    border-radius: 50%;
    border: 7px solid var(--ring);
    background: var(--white);
    padding: 5px;
  }
  .portrait {
    width: 100%;
    height: 100%;
    border-radius: 50%;
    background: radial-gradient(circle at 50% 45%, var(--photo-dark) 0%, #a88672 38%, var(--photo-light) 70%);
  }
  .member-role {
    margin-top: 26px;
    font-size: 29px;
    font-weight: 700;
    color: var(--accent);
  }
  .member-bio {
    margin-top: 10px;
    font-size: 21.5px;
    line-height: 33px;
    color: var(--navy);
  }
  .footer-band {
    position: absolute;
    left: 0;
    bottom: 0;
    width: 1200px;
    height: 27px;
    background: var(--footer-band);
  }
</style>
</head>
<body>
  <main class="slide">
    <div class="brand-name">Brevik Hamna</div>

    <h1 class="slide-title">OUR <strong>TEAM</strong></h1>
    <div class="title-rule"></div>

    <section class="team-member first">
      <div class="portrait-frame">
        <div class="portrait" role="img" aria-label="Portrait photo of a team member"></div>
      </div>
      <h2 class="member-role">Subtext here</h2>
      <p class="member-bio">Lorem Ipsum is simply dummy text<br>of the printing and typesetting<br>industry. Lorem Ipsum has been the<br>industry's standard dummy text</p>
    </section>

    <section class="team-member second">
      <div class="portrait-frame">
        <div class="portrait" role="img" aria-label="Portrait photo of a team member"></div>
      </div>
      <h2 class="member-role">Subtext here</h2>
      <p class="member-bio">Lorem Ipsum is simply dummy text<br>of the printing and typesetting<br>industry. Lorem Ipsum has been the<br>industry's standard dummy text</p>
    </section>

    <section class="team-member third">
      <div class="portrait-frame">
        <div class="portrait" role="img" aria-label="Portrait photo of a team member"></div>
      </div>
      <h2 class="member-role">Subtext here</h2>
      <p class="member-bio">Lorem Ipsum is simply dummy text<br>of the printing and typesetting<br>industry. Lorem Ipsum has been the<br>industry's standard dummy text</p>
    </section>

    <div class="footer-band"></div>
  </main>
</body>
</html>
```